Bref créative
Modern Business Card for Computer Service Company
Brightwave Tech Partners, Inc.
Professional
Marcus T. Hollings
Technology Engineer
4195 Larkin Avenue
Lakeview FL 33190
marcus@btp-helpdesk.com
www.btp-helpdesk.com
I would like a blurb that says "Serving Local Offices With Reliable IT Care"

```html
<!DOCTYPE html>
<html lang="en">
<head>
<meta charset="utf-8">
<title>Brightwave Tech Partners – Business Card</title>
<link href="https://fonts.googleapis.com/css2?family=Open+Sans:wght@400;600;700;800&display=swap" rel="stylesheet">
<style>
  :root {
    --navy: #0b2a6b;
    --blue: #1546a8;
    --blue-deep: #0a2d7a;
    --blue-light: #2f74d0;
    --green: #6bb536;
    --ink: #2a2f3a;
    --grey: #5a6170;
    --paper: #ffffff;
    --stage: #e9ecf0;
  }
  * { margin: 0; padding: 0; box-sizing: border-box; }
  html, body {
    width: 1200px; height: 1009px; overflow: hidden;
    background: var(--stage);
    font-family: "Open Sans", Arial, sans-serif;
  }
  .card {
    position: absolute; left: 200px; width: 800px; height: 457px;
    border-radius: 34px; overflow: hidden;
    box-shadow: 0 6px 18px rgba(0,0,0,.15);
  }
  .card--front { top: 34px; background: var(--paper); }
  .card--back {
    top: 518px;
    background: radial-gradient(ellipse at 50% 40%, var(--blue-light) 0%, var(--blue) 45%, var(--blue-deep) 100%);
  }
  .card__shapes { position: absolute; inset: 0; width: 100%; height: 100%; }

  .brand { position: absolute; left: 70px; top: 50px; display: flex; align-items: center; gap: 18px; }
  .brand__mark { width: 64px; height: 64px; border-radius: 50%; background: var(--blue); flex: none; }
  .brand__text { color: var(--navy); font-weight: 800; }
  .brand__name { display: block; font-size: 40px; line-height: 1; letter-spacing: 1px; }
  .brand__sub { display: block; font-size: 22px; line-height: 1.2; letter-spacing: 2px; margin-top: 4px; }
  .brand__tagline { display: block; font-size: 10px; letter-spacing: 1px; margin-top: 6px; }

  .person { position: absolute; left: 70px; top: 220px; }
  .person__name { color: var(--blue); font-size: 26px; font-weight: 600; }
  .person__title { color: var(--green); font-size: 18px; font-weight: 600; margin-top: 4px; }

  .contact { position: absolute; left: 440px; top: 200px; list-style: none; color: var(--ink); font-size: 17px; line-height: 1.55; }
  .contact li { display: flex; align-items: center; gap: 10px; }
  .contact svg { width: 14px; height: 14px; flex: none; fill: var(--grey); }
  .contact .plain { padding-left: 24px; }

  .back-brand { position: absolute; left: 0; right: 0; top: 160px; display: flex; justify-content: center; align-items: center; gap: 18px; }
  .back-brand__mark { width: 56px; height: 56px; background: var(--green); }
  .back-brand__name { color: #ffffff; font-weight: 800; font-size: 44px; letter-spacing: 1px; }
  .back-url { position: absolute; left: 0; right: 0; top: 250px; text-align: center; color: #ffffff; font-size: 15px; font-weight: 600; letter-spacing: 1px; }
</style>
</head>
<body>

<section class="card card--front" aria-label="Business card front">
  <svg class="card__shapes" viewBox="0 0 800 457" preserveAspectRatio="none" aria-hidden="true">
    <path d="M0 300 C120 360 260 420 360 457 L0 457 Z" fill="var(--blue)"/>
    <path d="M0 286 C130 350 270 410 380 457 L360 457 C260 420 120 360 0 300 Z" fill="var(--green)"/>
    <path d="M800 300 C720 370 620 430 520 457 L800 457 Z" fill="var(--blue)"/>
    <path d="M800 286 C715 362 610 425 500 457 L520 457 C620 430 720 370 800 300 Z" fill="var(--green)"/>
  </svg>

  <div class="brand">
    <span class="brand__mark"></span>
    <div class="brand__text">
      <span class="brand__name">BRIGHTWAVE</span>
      <span class="brand__sub">Tech Partners</span>
      <span class="brand__tagline">Serving Local Offices With Reliable IT Care</span>
    </div>
  </div>

  <div class="person">
    <p class="person__name">Marcus T. Hollings</p>
    <p class="person__title">Technology Engineer</p>
  </div>

  <ul class="contact">
    <li><svg viewBox="0 0 24 24"><path d="M12 2a7 7 0 0 0-7 7c0 5 7 13 7 13s7-8 7-13a7 7 0 0 0-7-7zm0 9.5A2.5 2.5 0 1 1 12 6.5a2.5 2.5 0 0 1 0 5z"/></svg>4195 Larkin Avenue</li>
    <li class="plain">Lakeview FL 33190</li>
    <li><svg viewBox="0 0 24 24"><path d="M6.6 10.8a15 15 0 0 0 6.6 6.6l2.2-2.2a1 1 0 0 1 1-.25 11.4 11.4 0 0 0 3.6.57 1 1 0 0 1 1 1V20a1 1 0 0 1-1 1A17 17 0 0 1 3 4a1 1 0 0 1 1-1h3.5a1 1 0 0 1 1 1c0 1.25.2 2.45.57 3.6a1 1 0 0 1-.25 1z"/></svg>954-555-0147</li>
    <li><svg viewBox="0 0 24 24"><path d="M4 4h16v12H4zM8 18h8v2H8z"/></svg>954-555-0192</li>
    <li><svg viewBox="0 0 24 24"><path d="M2 5h20v14H2zm2 2v.5l8 5 8-5V7z"/></svg>marcus@btp-helpdesk.com</li>
    <li><svg viewBox="0 0 24 24"><circle cx="12" cy="12" r="10"/></svg>www.btp-helpdesk.com</li>
  </ul>
</section>

<section class="card card--back" aria-label="Business card back">
  <div class="back-brand">
    <span class="back-brand__mark"></span>
    <span class="back-brand__name">BRIGHTWAVE</span>
  </div>
  <p class="back-url">www.btp-helpdesk.com</p>
</section>

</body>
</html>
```